Anzeigengestaltung für Gas- und Wasserinstallationsunternehmen
Zielgruppe
Gas- und Wasserinstallation, wir bauen, warten und sanieren Bäder und Heizungsanlagen
Wir wollen Leute im Alter 26-45 Jahre ansprechen, mit Berufserfahrung
Aufgabenstellung
Dass wir einen Kundendienstmonteur für Öl- und Gasfeuerung suchen

```html
<!DOCTYPE html>
<html lang="de">
<head>
<meta charset="utf-8">
<title>Stellenanzeige Kundendienstmonteur</title>
<link href="https://fonts.googleapis.com/css2?family=Open+Sans:wght@400;600;700&display=swap" rel="stylesheet">
<style>
  :root {
    --page-bg: #e6e6e6;
    --paper: #ffffff;
    --band-blue: #3a6db5;
    --band-teal: #4a8f8c;
    --band-green: #5aa845;
    --photo-red: #d9472f;
    --photo-red-dark: #b8311f;
    --photo-dark: #2c3440;
    --photo-blue: #34507a;
    --ink-blue: #3a6aa8;
    --ink-strong: #2f5f9e;
    --ink-green: #2e6b3a;
    --white: #ffffff;
  }
  * { box-sizing: border-box; margin: 0; padding: 0; }
  html, body {
    width: 1200px; height: 1200px; overflow: hidden;
    background: var(--page-bg);
    font-family: "Open Sans", Arial, sans-serif;
  }
  .ad {
    position: absolute; left: 190px; top: 20px;
    width: 820px; height: 1162px;
    background: var(--paper);
    overflow: hidden;
  }
  .band {
    position: absolute; left: 0; width: 100%;
    background: linear-gradient(90deg, var(--band-blue), var(--band-teal) 55%, var(--band-green));
  }
  .band--top { top: 0; height: 26px; }
  .band--bottom { top: 666px; height: 69px; }
  .hero-photo {
    position: absolute; left: 0; top: 26px; width: 100%; height: 640px;
    background:
      radial-gradient(ellipse at 78% 45%, var(--photo-blue) 0%, transparent 45%),
      linear-gradient(90deg, var(--photo-red) 0%, var(--photo-red-dark) 48%, var(--photo-dark) 62%, #3a4250 100%);
  }
  .headline {
    position: absolute; left: 47px; top: 172px;
    color: var(--white);
    font-size: 88px; line-height: 100px; font-weight: 400;
    letter-spacing: 0.5px;
  }
  .headline strong { font-weight: 700; }
  .job-title {
    position: absolute; left: 47px; top: 776px;
    color: var(--ink-blue);
    font-size: 38px; line-height: 49px; font-weight: 400;
  }
  .job-title strong { font-weight: 700; color: var(--ink-strong); }
  .copy {
    position: absolute; top: 902px;
    color: var(--ink-blue);
    font-size: 12.2px; line-height: 16.8px;
    white-space: nowrap;
  }
  .copy--intro { left: 47px; }
  .copy--apply { left: 413px; }
  .copy strong { font-weight: 700; }
  .contact {
    position: absolute; left: 47px; top: 1028px;
    color: var(--ink-blue);
    font-size: 13.2px; line-height: 16.8px;
    font-style: normal;
  }
  .contact strong { font-weight: 700; }
  .brand {
    position: absolute; right: 42px; top: 1060px;
    display: flex; align-items: center; gap: 16px;
  }
  .brand__dot {
    width: 46px; height: 46px; border-radius: 50%;
    background: var(--band-blue);
  }
  .brand__name {
    color: var(--ink-green);
    font-size: 29px; font-weight: 700; letter-spacing: 0.3px;
  }
</style>
</head>
<body>
  <main class="ad">
    <div class="band band--top"></div>
    <div class="hero-photo" role="img" aria-label="Foto: lächelnder Monteur im blauen Arbeitshemd neben einem roten Heizungskessel im Technikraum"></div>
    <h1 class="headline">Sie bleiben<br><strong>cool,</strong> auch<br>wenn es mal<br><strong>heiß</strong> hergeht?</h1>
    <div class="band band--bottom"></div>

    <h2 class="job-title">Erfahrenen Kundendienstmonteur<br>für <strong>Öl- und Gasfeuerung</strong> gesucht</h2>

    <p class="copy copy--intro">Wir suchen für unser Team einen erfahrenen Kundendienst-<br>monteur für Öl- und Gasfeuerung. Sie haben Lust auf an-<br>spruchvolle Aufgaben in einem modernen Betrieb? Mitten<br>in Berlin erwartet Sie ein tolles Team, ein gutes Arbeitsklima<br>und eine angemessene Bezahlung.</p>

    <p class="copy copy--apply"><strong>Bewerbung mit aussagekräftigen Unterlagen</strong><br>(Anschreiben, Lebenslauf mit Lichtbild, Zeugnissen) bitte<br>schriftlich an: Wärmewerk3000 GmbH, Gesellschaft für<br>Heiztechnik mbH, Lindenhofer Str. 14, 10437 Berlin oder<br>per PDF, Mail: info@waermewerk3000-gmbh.de</p>

    <address class="contact">
      <strong>Gesellschaft für Heiztechnik mbH</strong><br>
      Lindenhofer Str. 14<br>
      10437 Berlin<br>
      Tel.: +49 (0)30 12 34-5600<br>
      <strong>www.waermewerk3000-gmbh.de</strong>
    </address>

    <div class="brand">
      <span class="brand__dot"></span>
      <span class="brand__name">WÄRMEWERK3000 GMBH</span>
    </div>
  </main>
</body>
</html>
```